Menubook for a 2star restaurant

Hey,
We are looking for a new menu for a 2 star restaurant in Belgium. They want a clean, abstract, with small light accents of gold, copper. The format will be 21 cm by 21 cm. and the booklet will have 4 printable sides inc front & back. Only the logo on the front. The wine list will be separate so it should not be included in the design. "Bites" - "voorgerechten" - "hoofdgerechten" & "nagerechten" must be copied.

Industry/Entity Type

Restaurant

Requirements
Must have
• Clean look
Nice to have
• touches of gold

```html
<!DOCTYPE html>
<html lang="nl">
<head>
<meta charset="utf-8">
<title>Menukaart – twee uitvoeringen</title>
<link rel="stylesheet" href="https://fonts.googleapis.com/css2?family=Montserrat:ital,wght@0,300;0,400;0,500;0,700;0,900;1,300&display=swap">
<style>
:root{
  --backdrop:#efefef;
  --paper:#ffffff;
  --ink:#111111;
  --ink-soft:#2b2b2b;
  --muted:#777777;
  --on-grey:#e9e9e9;
  --wash-light:#a9a9ab;
  --wash-mid:#909092;
  --wash-dark:#7d7d80;
  --gold:#c9a95c;
  --gold-light:#e6d296;
}
*{margin:0;padding:0;box-sizing:border-box}
html,body{width:1200px;height:657px;overflow:hidden;background:var(--backdrop);
  font-family:"Montserrat",Arial,sans-serif;color:var(--ink)}
.spread{position:absolute;top:55px;width:546px;height:545px;background:var(--paper);
  box-shadow:0 1px 4px rgba(0,0,0,.25);overflow:hidden}
.spread--panel{left:47px}
.spread--brush{left:595px}
.wash-panel{position:absolute;left:272px;top:0;width:274px;height:545px;
  background:linear-gradient(90deg,var(--wash-light),var(--wash-mid) 40%,var(--wash-light) 70%,var(--wash-mid));}
.wash-brush{position:absolute;left:257px;top:8px;width:285px;height:537px;
  border-radius:22px 6px 0 30px;
  background:linear-gradient(100deg,var(--wash-dark),var(--wash-mid) 35%,var(--wash-light) 60%,var(--wash-mid));}
.menu-box{position:absolute;left:16px;width:240px;border:1px solid var(--ink)}
.menu-box--bites{top:50px;height:198px}
.menu-box--starters{top:265px;height:123px}
.menu-box--desserts{top:405px;height:90px}
.menu-box--mains{left:289px;top:80px;width:238px;height:361px;border:2px solid var(--gold);
  border-image:linear-gradient(135deg,var(--gold),var(--gold-light),var(--gold)) 1}
.section-title{position:absolute;left:8px;transform:translateY(-50%);
  font-weight:900;font-size:10.5px;letter-spacing:4px;line-height:1}
.row{position:absolute;left:8px;right:8px;display:flex;justify-content:space-between;
  align-items:center;transform:translateY(-50%);line-height:1}
.dish{font-size:9.2px;letter-spacing:1.1px;font-weight:400;color:var(--ink-soft)}
.note{font-size:8.3px;font-weight:300;color:var(--muted)}
.price{font-size:9px;font-weight:700}
.menu-box--bites .price{margin-right:8px}
.menu-box--mains .dish{color:var(--ink-soft)}
.menu-box--mains .note{color:var(--on-grey)}
.menu-box--mains .price{color:var(--ink)}
.tasting-note{position:absolute;left:300px;width:216px;top:452px;text-align:center;
  transform:translateY(-50%);font-size:8px;font-style:italic;font-weight:300;color:var(--ink-soft)}
</style>
</head>
<body>

<section class="spread spread--panel">
  <div class="wash-panel" role="img" aria-label="Grijze aquarel-textuur"></div>

  <div class="menu-box menu-box--bites">
    <h2 class="section-title" style="top:21px">BITES</h2>
    <div class="row" style="top:45px"><span class="dish">OESTER LAMBRECHT (1st)</span></div>
    <div class="row" style="top:61px"><span class="note">jalapeño | komkommer | ajo blanco</span><span class="price">9</span></div>
    <div class="row" style="top:72px"><span class="note">(supplement kaviaar 5gr + €18)</span></div>
    <div class="row" style="top:94px"><span class="dish">‘nduja RISOTTO CROQUETTES (2nd)</span><span class="price">9</span></div>
    <div class="row" style="top:119px"><span class="dish">CHARCUTERIE</span></div>
    <div class="row" style="top:135px"><span class="note">cornichon | olijven</span><span class="price">9</span></div>
    <div class="row" style="top:160px"><span class="dish">KOUDE AMANDEL-KNOFLOOK ZUPPA</span></div>
    <div class="row" style="top:176px"><span class="note">fregola | kreeft</span><span class="price">9</span></div>
  </div>

  <div class="menu-box menu-box--starters">
    <h2 class="section-title" style="top:20px">VOORGERECHTEN</h2>
    <div class="row" style="top:44px"><span class="dish">ANTIPASTI**</span><span class="price">35</span></div>
    <div class="row" style="top:70px"><span class="dish">PIZETTA AMARO</span></div>
    <div class="row" style="top:85px"><span class="note">met 1/2 kreeft | doperwt | basilicum | courgette</span><span class="price">37</span></div>
    <div class="row" style="top:102px"><span class="note">ook vegetarisch te bestellen</span><span class="price">32</span></div>
  </div>

  <div class="menu-box menu-box--desserts">
    <h2 class="section-title" style="top:20px">NAGERECHTEN</h2>
    <div class="row" style="top:44px"><span class="dish">ASSORTIMENT VAN 5 ITALIAANSE KAZEN</span><span class="price">27</span></div>
    <div class="row" style="top:69px"><span class="dish">AMALFI CITROEN MET MERINGUE**</span><span class="price">16</span></div>
  </div>

  <div class="menu-box menu-box--mains">
    <h2 class="section-title" style="top:20px">HOOFDEGERECHTEN</h2>
    <div class="row" style="top:52px"><span class="dish">KALFSFILET**</span></div>
    <div class="row" style="top:69px"><span class="note">paarse bloemkool | girolle | groen asperge</span><span class="price">46</span></div>
    <div class="row" style="top:80px"><span class="note">daslook | pijpajuin</span></div>
    <div class="row" style="top:110px"><span class="dish">SPAGHETTI VONGOLE **</span></div>
    <div class="row" style="top:126px"><span class="note">bosui | piemento | zilte groenten</span><span class="price">29</span></div>
    <div class="row" style="top:159px"><span class="dish">KABELJAUW RUG **</span></div>
    <div class="row" style="top:176px"><span class="note">limoen | kappertjes | mosselen | safraan</span><span class="price">36</span></div>
    <div class="row" style="top:209px"><span class="dish">GNOCCHI</span></div>
    <div class="row" style="top:225px"><span class="note">salie | spinazie | barilotto</span><span class="price">29</span></div>
    <div class="row" style="top:258px"><span class="dish">GEPOCHEERD HOEVE EI</span></div>
    <div class="row" style="top:274px"><span class="note">girolle | daslook | groene asperges</span><span class="price">36</span></div>
    <div class="row" style="top:308px"><span class="dish">INSALATE DEL GIORNO</span></div>
    <div class="row" style="top:324px"><span class="note">vlees of vis</span><span class="price">40</span></div>
    <div class="row" style="top:340px"><span class="note">veggie</span><span class="price">33</span></div>
  </div>
  <p class="tasting-note">** Menu (5 Gangen)..........................95</p>
</section>

<section class="spread spread--brush">
  <div class="wash-brush" role="img" aria-label="Grijze penseelstreek in aquarel"></div>

  <div class="menu-box menu-box--bites">
    <h2 class="section-title" style="top:21px">BITES</h2>
    <div class="row" style="top:45px"><span class="dish">OESTER LAMBRECHT (1st)</span></div>
    <div class="row" style="top:61px"><span class="note">jalapeño | komkommer | ajo blanco</span><span class="price">9</span></div>
    <div class="row" style="top:72px"><span class="note">(supplement kaviaar 5gr + €18)</span></div>
    <div class="row" style="top:94px"><span class="dish">‘nduja RISOTTO CROQUETTES (2nd)</span><span class="price">9</span></div>
    <div class="row" style="top:119px"><span class="dish">CHARCUTERIE</span></div>
    <div class="row" style="top:135px"><span class="note">cornichon | olijven</span><span class="price">9</span></div>
    <div class="row" style="top:160px"><span class="dish">KOUDE AMANDEL-KNOFLOOK ZUPPA</span></div>
    <div class="row" style="top:176px"><span class="note">fregola | kreeft</span><span class="price">9</span></div>
  </div>

  <div class="menu-box menu-box--starters">
    <h2 class="section-title" style="top:20px">VOORGERECHTEN</h2>
    <div class="row" style="top:44px"><span class="dish">ANTIPASTI**</span><span class="price">35</span></div>
    <div class="row" style="top:70px"><span class="dish">PIZETTA AMARO</span></div>
    <div class="row" style="top:85px"><span class="note">met 1/2 kreeft | doperwt | basilicum | courgette</span><span class="price">37</span></div>
    <div class="row" style="top:102px"><span class="note">ook vegetarisch te bestellen</span><span class="price">32</span></div>
  </div>

  <div class="menu-box menu-box--desserts">
    <h2 class="section-title" style="top:20px">NAGERECHTEN</h2>
    <div class="row" style="top:44px"><span class="dish">ASSORTIMENT VAN 5 ITALIAANSE KAZEN</span><span class="price">27</span></div>
    <div class="row" style="top:69px"><span class="dish">AMALFI CITROEN MET MERINGUE**</span><span class="price">16</span></div>
  </div>

  <div class="menu-box menu-box--mains">
    <h2 class="section-title" style="top:20px">HOOFDEGERECHTEN</h2>
    <div class="row" style="top:52px"><span class="dish">KALFSFILET**</span></div>
    <div class="row" style="top:69px"><span class="note">paarse bloemkool | girolle | groen asperge</span><span class="price">46</span></div>
    <div class="row" style="top:80px"><span class="note">daslook | pijpajuin</span></div>
    <div class="row" style="top:110px"><span class="dish">SPAGHETTI VONGOLE **</span></div>
    <div class="row" style="top:126px"><span class="note">bosui | piemento | zilte groenten</span><span class="price">29</span></div>
    <div class="row" style="top:159px"><span class="dish">KABELJAUW RUG **</span></div>
    <div class="row" style="top:176px"><span class="note">limoen | kappertjes | mosselen | safraan</span><span class="price">36</span></div>
    <div class="row" style="top:209px"><span class="dish">GNOCCHI</span></div>
    <div class="row" style="top:225px"><span class="note">salie | spinazie | barilotto</span><span class="price">29</span></div>
    <div class="row" style="top:258px"><span class="dish">GEPOCHEERD HOEVE EI</span></div>
    <div class="row" style="top:274px"><span class="note">girolle | daslook | groene asperges</span><span class="price">36</span></div>
    <div class="row" style="top:308px"><span class="dish">INSALATE DEL GIORNO</span></div>
    <div class="row" style="top:324px"><span class="note">vlees of vis</span><span class="price">40</span></div>
    <div class="row" style="top:340px"><span class="note">veggie</span><span class="price">33</span></div>
  </div>
  <p class="tasting-note">** Menu (5 Gangen)..........................95</p>
</section>

</body>
</html>
```